Semi Permanent make up flyer

Hi

I will be sending a few thousand flyers dropped door to door in some very lovely parts of London.

The flyer must contain the following information;

New studio in Greenwich

Velmira Lineo trained technician - gold advanced level

Free consultation no obligation

Price List;
Eyebrow hair stroke: £325
Eyebrows 3D effect: £395
Microblading hair stroke: £330
Eyelash enhancement Top: £250
Eyelash enhancement Top & Bottom: £300
Lip blush: £450

Tel;……………….
Facebook: Odelie Permanent Cosmetics
Instagram: Odelie_Permanent_Cosmetics

Special introductory offers - available for a limited time only;
Like & share my page for 10% off any treatment
Refer a friend for £50 off each
Buy one treatment get 50% off another

I would like it to look clean, professional, expensive, and high end/luxury

I’m happy to make this a double sided print so I can have my logo on the front and the information on the back.

It must include my logo.

If you could use images of appealing women I think it would work best. Images have to have nice eyes, lips and brows. Weather you use entire face or features that is up to you.

Please show me a selection of different colour ways across the whole design. I personally feel softer tones would work. No black or bright colours.

I will be getting my new phone number in the next few days. I will let you know via messages what it is for you to add it in.

Any questions feel free to ask.

Target Market(s)

Women

Industry/Entity Type

Beauty Salon

Font styles to use
Sans Serif

Requirements
Must have
• Everything in Description
Nice to have
• The designers give their ideas. Im looking for input
Should not have
• Childish, cheap images or fonts. This is very high end so needs to look it

```html
<!DOCTYPE html>
<html lang="en">
<head>
<meta charset="utf-8">
<title>Odelie Permanent Cosmetics – Flyer</title>
<link rel="stylesheet" href="https://fonts.googleapis.com/css2?family=Rubik:wght@300;400&family=Arimo:wght@400;700&display=swap">
<style>
  :root {
    --backdrop: #ece7e2;
    --paper: #ffffff;
    --gold: #c9a14a;
    --gold-light: #e8c873;
    --gold-deep: #a67c2e;
    --rose: #c2393f;
    --ink: #2b2b2b;
    --skin-light: #f4d9cf;
    --skin-mid: #e8b7a8;
    --petal: #d9798f;
    --hair: #5a2f22;
  }
  * { margin: 0; padding: 0; box-sizing: border-box; }
  html, body { width: 1200px; height: 860px; overflow: hidden; background: var(--backdrop); }
  .stage { position: relative; width: 1200px; height: 860px; }

  .flyer {
    position: absolute; top: 80px; width: 492px; height: 698px;
    background: var(--paper); overflow: hidden;
    box-shadow: 0 4px 14px rgba(0,0,0,.18);
  }
  .flyer--front { left: 88px; }
  .flyer--back { left: 620px; }

  /* Front */
  .front-photo {
    position: absolute; left: 0; top: 0; width: 492px; height: 520px;
    background:
      radial-gradient(ellipse 45% 30% at 85% 15%, var(--petal) 0%, rgba(217,121,143,0) 70%),
      radial-gradient(ellipse 60% 55% at 45% 40%, var(--skin-light) 0%, var(--skin-mid) 70%, #c98f80 100%);
  }
  .front-accent {
    position: absolute; left: 0; top: 500px; width: 492px; height: 198px;
    background: linear-gradient(120deg, var(--gold-deep) 0%, var(--gold-light) 45%, var(--gold) 100%);
  }
  .front-panel {
    position: absolute; left: 24px; top: 540px; width: 468px; height: 158px;
    background: var(--paper);
    border-top-left-radius: 240px 150px;
  }
  .front-brand { position: absolute; left: 0; right: 0; top: 598px; text-align: center; font-family: "Rubik", sans-serif; }
  .brand-name { color: var(--gold); font-weight: 300; letter-spacing: 5px; }
  .brand-tagline { color: var(--gold); font-weight: 400; letter-spacing: 1.5px; text-transform: uppercase; }
  .front-brand .brand-name { font-size: 14px; }
  .front-brand .brand-tagline { font-size: 6.5px; margin-top: 1px; }
  .brand-mark { width: 22px; height: 22px; border-radius: 50%; background: var(--gold); }
  .front-brand .brand-mark { margin: 0 auto 12px; }
  .front-tel { font-family: "Arimo", sans-serif; font-size: 7px; color: var(--ink); margin-top: 6px; }

  /* Back */
  .back-photo {
    position: absolute; top: 0; right: 0; width: 300px; height: 698px;
    background:
      radial-gradient(ellipse 60% 42% at 62% 42%, var(--skin-light) 0%, #e2b6a3 60%, rgba(226,182,163,0) 100%),
      radial-gradient(ellipse 70% 25% at 70% 8%, var(--hair) 0%, rgba(90,47,34,0) 100%),
      linear-gradient(90deg, rgba(255,255,255,1) 0%, rgba(244,236,232,.6) 30%, #efe2da 100%);
  }
  .back-content { position: absolute; left: 46px; top: 0; width: 260px; font-family: "Arimo", sans-serif; color: var(--ink); }
  .back-brand { position: absolute; top: 100px; font-family: "Rubik", sans-serif; }
  .back-brand .brand-mark { margin: 0 0 8px 24px; }
  .back-brand .brand-name { font-size: 14px; }
  .back-brand .brand-tagline { font-size: 7px; margin-top: 2px; }
  .headline {
    position: absolute; top: 184px; width: 240px;
    font-family: "Rubik", sans-serif; font-weight: 300;
    font-size: 35px; line-height: 36px; color: var(--rose);
  }
  .intro { position: absolute; top: 272px; font-size: 9.5px; line-height: 12px; }
  .intro p + p { margin-top: 12px; }
  .price-list { position: absolute; top: 345px; width: 206px; font-size: 10.5px; line-height: 12.6px; }
  .price-list h2 { font-weight: 400; font-size: 11px; margin-bottom: 1px; }
  .price-row { display: flex; justify-content: space-between; }
  .price-row .price { color: var(--rose); font-weight: 700; }
  .offers { position: absolute; top: 454px; font-size: 9.8px; line-height: 11.6px; }
  .contact { position: absolute; top: 566px; font-size: 10px; line-height: 12.4px; }
  .contact .tel { font-weight: 700; color: var(--rose); font-size: 13.5px; margin-bottom: 3px; }
  .social { display: flex; align-items: center; gap: 4px; }
  .social-dot { width: 8px; height: 8px; background: var(--rose); }
  .social-dot--round { border-radius: 50%; }
</style>
</head>
<body>
<main class="stage">

  <section class="flyer flyer--front" aria-label="Flyer front">
    <div class="front-photo" role="img" aria-label="Close-up beauty portrait of a woman with soft pink make-up and pink orchids"></div>
    <div class="front-accent" role="img" aria-label="Flowing gold ribbon decoration"></div>
    <div class="front-panel"></div>
    <div class="front-brand">
      <div class="brand-mark"></div>
      <div class="brand-name">ODELIE</div>
      <div class="brand-tagline">Permanent Cosmetics</div>
      <div class="front-tel">Tel 000 00 000 00</div>
    </div>
  </section>

  <section class="flyer flyer--back" aria-label="Flyer back">
    <div class="back-photo" role="img" aria-label="Portrait of a woman with sleek auburn hair, smoky eyes and red lips"></div>
    <div class="back-content">
      <div class="back-brand">
        <div class="brand-mark"></div>
        <div class="brand-name">ODELIE</div>
        <div class="brand-tagline">Permanent Cosmetics</div>
      </div>
      <h1 class="headline">New studio in Greenwich</h1>
      <div class="intro">
        <p>Velmira Lineo trained technician<br>gold advanced level</p>
        <p>Free consultation no obligation</p>
      </div>
      <div class="price-list">
        <h2>Price List</h2>
        <div class="price-row"><span>Eyebrow hair stroke</span><span class="price">£325</span></div>
        <div class="price-row"><span>Eyebrows 3D effect</span><span class="price">£395</span></div>
        <div class="price-row"><span>Microblading hair stroke</span><span class="price">£330</span></div>
        <div class="price-row"><span>Eyelash enhancement Top</span><span class="price">£250</span></div>
        <div class="price-row"><span>Eyelash enhancement Top &amp; Bottom</span><span class="price">£300</span></div>
        <div class="price-row"><span>Lip blush</span><span class="price">£450</span></div>
      </div>
      <div class="offers">
        <p>Special introductory offers</p>
        <p>available for a limited time only</p>
        <p>Like &amp; share my page for 10% off any treatment</p>
        <p>Refer a friend for £50 off each</p>
        <p>Buy one treatment get 50% off another</p>
      </div>
      <div class="contact">
        <p class="tel">Tel: 000 00 000 00</p>
        <p class="social"><span class="social-dot"></span>Odelie Permanent Cosmetics</p>
        <p class="social"><span class="social-dot social-dot--round"></span>Odelie_Permanent_Cosmetics</p>
      </div>
    </div>
  </section>

</main>
</body>
</html>
```